Marlo Tidy Yard Website

We need a website design for this new company. I've attached the company logo. This company is in the construction industry that provides general labor, maintenance and cleaning for construction sites. We want a clean and simple website that can be easy to navigate.

Target Market(s)

Construction industry

Industry/Entity Type

Construction

Number of Pages Required

2 page

Font styles to use
Sans Serif

```html
<!DOCTYPE html>
<html lang="en">
<head>
<meta charset="utf-8">
<title>Marlo Tidy Yard</title>
<link rel="stylesheet" href="https://fonts.googleapis.com/css2?family=Poppins:wght@400;500;600;700&family=Open+Sans:wght@400;600&display=swap">
<style>
:root{
  --yellow:#f0b417;
  --yellow-dark:#d89e08;
  --navy:#1f2b45;
  --navy-deep:#18223a;
  --ink:#1b1b1b;
  --muted:#8a8a8a;
  --line:#e6e6e6;
  --soft:#f6f6f6;
  --white:#ffffff;
}
*{box-sizing:border-box;margin:0;padding:0}
html,body{width:1200px;height:3651px;overflow:hidden}
body{font-family:"Open Sans",Arial,sans-serif;color:var(--ink);background:var(--white);font-size:12px;line-height:1.6}
h1,h2,h3,h4,.brand,.nav{font-family:"Poppins",Arial,sans-serif}
.page{position:relative;width:1200px;height:3651px}

/* header */
.site-header{height:90px;display:flex;align-items:center;padding:0 243px;justify-content:space-between}
.brand{display:flex;align-items:center;gap:8px;font-weight:700;font-size:16px;color:var(--navy)}
.brand-mark{width:16px;height:16px;background:var(--yellow)}
.nav{display:flex;gap:36px;font-size:10px;font-weight:500;color:#333;align-items:center;letter-spacing:.5px}
.nav .active{color:var(--yellow)}

/* hero */
.hero{height:282px;background:linear-gradient(100deg,#2b2320 0%,#5a4a3a 35%,#8a8684 60%,#3a3a3c 100%);position:relative}
.hero-arrow{position:absolute;top:130px;width:20px;height:20px;color:#fff;font-size:18px;line-height:20px;text-align:center}

/* about */
.about{height:418px;position:relative}
.about-box{position:absolute;top:-31px;left:226px;width:748px;height:414px;display:flex}
.about-text{width:373px;background:var(--yellow);padding:38px 40px;color:#2b2200}
.eyebrow{font-size:8px;letter-spacing:1px;text-transform:uppercase;color:#555}
.about-text h2{font-size:17px;font-weight:700;color:#1b1b1b;margin:2px 0 42px}
.about-text p{font-size:11px;color:#3a2f00}
.about-quote{display:flex;gap:12px;margin-top:22px}
.quote-mark{font-family:"Poppins",sans-serif;font-size:40px;line-height:34px;color:#6b5300}
.about-quote p{font-size:14px;line-height:1.65;color:#5a4700}
.signature{margin-top:34px;width:80px;height:2px;background:#3a2f00}
.about-photo{flex:1;background:linear-gradient(180deg,#2a6cc4 0%,#3d7fd0 45%,#b57a3e 75%,#4a3420 100%)}

/* section heads */
.section-head{text-align:center}
.section-head .eyebrow{font-size:8px;color:var(--muted)}
.section-head h2{font-size:15px;font-weight:700;letter-spacing:.5px;margin-top:2px}

/* industry */
.industry{height:270px;padding-top:8px}
.industry-grid{display:flex;justify-content:center;gap:60px;margin-top:40px}
.industry-item{width:180px;text-align:center}
.industry-item svg{width:40px;height:40px}
.industry-item h3{font-size:9px;font-weight:700;margin:10px 0 4px;text-transform:uppercase}
.industry-item p{font-size:9px;color:var(--muted);line-height:1.5}

/* projects */
.projects{height:568px;padding-top:38px}
.filters{display:flex;justify-content:center;gap:28px;margin-top:22px;font-size:8px;color:var(--muted);text-transform:uppercase}
.filters .on{color:var(--yellow);border-bottom:1px solid var(--yellow)}
.project-grid{display:grid;grid-template-columns:repeat(3,244px);grid-template-rows:180px 180px;width:732px;margin:34px auto 0}
.project-grid div:nth-child(1){background:linear-gradient(135deg,#c8521c,#7a4a30)}
.project-grid div:nth-child(2){background:linear-gradient(180deg,#2a64b8,#9ab6d8 70%,#e0e6ee)}
.project-grid div:nth-child(3){background:linear-gradient(180deg,#d9852a,#3a2a20)}
.project-grid div:nth-child(4){background:linear-gradient(135deg,#1d2a24,#3f8a5a 50%,#1a1a1a)}
.project-grid div:nth-child(5){background:linear-gradient(180deg,#6b6c6f,#2c2e33)}
.project-grid div:nth-child(6){background:linear-gradient(180deg,#2e6fc2,#c48a3a 70%,#5a3a22)}

/* features */
.features{height:458px;background:var(--navy);color:#fff;position:relative;padding-top:52px}
.features .section-head .eyebrow{color:var(--yellow)}
.features .section-head h2{color:#fff}
.feature{position:absolute;width:250px;display:flex;gap:12px;align-items:flex-start}
.feature h3{font-size:8px;font-weight:700;text-transform:uppercase;margin-bottom:4px}
.feature p{font-size:8px;color:#aab2c2;line-height:1.5}
.feature svg{width:28px;height:28px;flex:none}
.feature.left{left:212px;text-align:right;justify-content:flex-end}
.feature.right{left:742px}
.worker{position:absolute;left:487px;top:137px;width:226px;height:321px;background:linear-gradient(180deg,#1f2b45 0%,#c8a070 30%,#9a6a3a 60%,#5a4a32 100%)}

/* posts */
.posts{height:409px;padding-top:40px}
.post-grid{display:flex;gap:20px;justify-content:center;margin-top:30px}
.post{width:226px}
.post-img{height:122px}
.post:nth-child(1) .post-img{background:linear-gradient(180deg,#6a7480,#c7b58a 60%,#6a5230)}
.post:nth-child(2) .post-img{background:linear-gradient(180deg,#2a66c0,#8aa6c6 60%,#b8c2cc)}
.post:nth-child(3) .post-img{background:linear-gradient(180deg,#2a5fb0,#8a3a28 55%,#5a2a1e)}
.post-meta{font-size:8px;color:var(--muted);margin:10px 0 3px}
.post-meta b{color:var(--yellow);font-weight:400}
.post h3{font-size:11px;font-weight:600;line-height:1.35;margin-bottom:8px}
.post p{font-size:8px;color:var(--muted);line-height:1.55}

/* testimonials */
.testimonials{height:353px;background:var(--soft);padding-top:52px}
.quote-grid{display:flex;gap:20px;justify-content:center;margin-top:36px}
.quote-card{width:356px}
.quote-badge{width:24px;height:24px;background:var(--yellow);color:#fff;font-family:"Poppins",sans-serif;font-size:20px;line-height:30px;text-align:center;margin-bottom:14px}
.quote-card p{font-size:11px;color:#555;line-height:1.6}
.author{display:flex;gap:12px;align-items:center;margin-top:22px}
.avatar{width:64px;height:42px;background:linear-gradient(135deg,#b9a48a,#6a5a4a)}
.author h4{font-size:12px;font-weight:600}
.author span{font-size:8px;color:var(--muted)}

/* partners */
.partners{height:97px;display:flex;align-items:center;justify-content:center;gap:70px}
.partner{width:80px;height:22px;background:#c9c9c9;border-radius:3px}
.partner.round{width:26px;height:26px;border-radius:50%}

/* map */
.map{height:346px;padding:0 10px}
.map-area{height:346px;background:linear-gradient(160deg,#5a6470 0%,#2f4a66 45%,#3a5672 70%,#59636d 100%);position:relative}
.map-pin{position:absolute;left:588px;top:150px;width:16px;height:22px}

/* contact */
.contact{height:282px;padding-top:42px;position:relative}
.contact-brand{position:absolute;left:97px;top:148px}
.contact-cols{display:flex;justify-content:center;gap:60px;margin-top:30px;padding-left:40px}
.contact-col{width:200px;text-align:center}
.contact-icon{width:30px;height:30px;background:var(--yellow);margin:0 auto 12px;display:flex;align-items:center;justify-content:center}
.contact-icon svg{width:14px;height:14px}
.contact-col h3{font-size:12px;font-weight:700;text-transform:uppercase;margin-bottom:6px}
.contact-col p{font-size:8px;color:var(--muted);line-height:1.55}
.contact-col .value{color:var(--yellow-dark);margin-top:8px}

/* footer */
.site-footer{height:78px;background:var(--navy-deep);display:flex;align-items:center;justify-content:flex-end;padding-right:250px;gap:18px}
.social-dot{width:8px;height:8px;border-radius:50%;background:#7f8899}
</style>
</head>
<body>
<div class="page">

<header class="site-header">
  <div class="brand"><span class="brand-mark"></span>Marlo Tidy Yard</div>
  <nav class="nav">
    <span class="active">HOME ▾</span><span>SERVICES ▾</span><span>PROJECT ▾</span><span>NEW ▾</span><span>PAGE ▾</span><span>THEME ▾</span>
    <svg width="11" height="11" viewBox="0 0 12 12"><circle cx="5" cy="5" r="3.8" fill="none" stroke="#333" stroke-width="1.5"/><line x1="8" y1="8" x2="11" y2="11" stroke="#333" stroke-width="1.5"/></svg>
  </nav>
</header>

<section class="hero" role="img" aria-label="Welder at work with sparks flying in a workshop">
  <span class="hero-arrow" style="left:14px">‹</span>
  <span class="hero-arrow" style="right:14px">›</span>
</section>

<section class="about">
  <div class="about-box">
    <div class="about-text">
      <div class="eyebrow">About us</div>
      <h2>WHO WE ARE</h2>
      <p>Continually embrace bricks and clicks scenarios via premium synergy. Uniquely transform competitive applications through corporate influence.</p>
      <div class="about-quote">
        <span class="quote-mark">“</span>
        <p>We work with our partners to streamline project plans that don't just deliver on product perfection, but also delivers on time – crucial to success in a highly competitive market where every day counts.</p>
      </div>
      <div class="signature"></div>
    </div>
    <div class="about-photo" role="img" aria-label="Modern glass building lit at dusk"></div>
  </div>
</section>

<section class="industry">
  <div class="section-head"><div class="eyebrow">Services</div><h2>OUR INDUSTRY TARGET</h2></div>
  <div class="industry-grid">
    <div class="industry-item">
      <svg viewBox="0 0 40 40" fill="none" stroke="#333" stroke-width="1.5"><rect x="8" y="24" width="24" height="12"/><line x1="16" y1="24" x2="16" y2="8"/><line x1="16" y1="8" x2="30" y2="14"/><circle cx="30" cy="16" r="2"/></svg>
      <h3>Automotive Parts &amp; System</h3><p>Appropriately maintain mission critical applications for competitive schemas. Energistically...</p>
    </div>
    <div class="industry-item">
      <svg viewBox="0 0 40 40" fill="none" stroke="#333" stroke-width="1.5"><path d="M6 34V18L20 8l14 10v16z"/><line x1="12" y1="20" x2="12" y2="34"/><line x1="20" y1="20" x2="20" y2="34"/><line x1="28" y1="20" x2="28" y2="34"/></svg>
      <h3>Manual Welding</h3><p>Holistically impact reliable timely communities without an expanded array...</p>
    </div>
    <div class="industry-item">
      <svg viewBox="0 0 40 40" fill="none" stroke="#333" stroke-width="1.5"><circle cx="20" cy="16" r="9"/><line x1="14" y1="24" x2="10" y2="36"/><line x1="26" y1="24" x2="30" y2="36"/><line x1="8" y1="36" x2="32" y2="36"/></svg>
      <h3>Power and Energy</h3><p>Seamlessly enable end metrics whereas transparent market capital...</p>
    </div>
    <div class="industry-item">
      <svg viewBox="0 0 40 40" fill="none" stroke="#333" stroke-width="1.5"><circle cx="20" cy="20" r="10"/><circle cx="20" cy="20" r="4"/><line x1="6" y1="6" x2="34" y2="34"/><line x1="34" y1="6" x2="6" y2="34"/></svg>
      <h3>Material Engineering</h3><p>Conveniently expedite timely resources without ideating edge communities. Compellingly...</p>
    </div>
  </div>
</section>

<section class="projects">
  <div class="section-head"><div class="eyebrow">Works</div><h2>RECENT PROJECTS</h2></div>
  <div class="filters"><span class="on">All</span><span>Agriculture</span><span>Chemical</span><span>Materials</span><span>Mechanical</span><span>Power &amp; Energy</span></div>
  <div class="project-grid">
    <div role="img" aria-label="Worker in orange safety suit grinding metal"></div>
    <div role="img" aria-label="Pipeline running under a blue sky"></div>
    <div role="img" aria-label="Mine headframe against an orange sunset"></div>
    <div role="img" aria-label="Welder with green sparks in a dark workshop"></div>
    <div role="img" aria-label="Team of workers in yellow hard hats"></div>
    <div role="img" aria-label="Industrial plant lit against a blue sky"></div>
  </div>
</section>

<section class="features">
  <div class="section-head"><div class="eyebrow">Why choose us</div><h2>AWESOME FEATURES</h2></div>
  <div class="feature left" style="top:140px"><div><h3>Latest Technology</h3><p>Appropriately grow high-quality portals through reliable technology</p></div>
    <svg viewBox="0 0 28 28" fill="none" stroke="#f0b417" stroke-width="1.3"><circle cx="14" cy="14" r="11"/><circle cx="14" cy="14" r="5"/></svg></div>
  <div class="feature left" style="top:223px"><div><h3>Profesional Workers</h3><p>Appropriately grow high-quality portals through reliable technology</p></div>
    <svg viewBox="0 0 28 28" fill="none" stroke="#f0b417" stroke-width="1.3"><circle cx="14" cy="10" r="5"/><path d="M5 26c0-6 4-9 9-9s9 3 9 9"/></svg></div>
  <div class="feature left" style="top:308px"><div><h3>Maintenance</h3><p>Appropriately grow high-quality portals through reliable technology</p></div>
    <svg viewBox="0 0 28 28" fill="none" stroke="#f0b417" stroke-width="1.3"><path d="M4 24l12-12M16 6a6 6 0 0 0 6 8"/><rect x="4" y="4" width="6" height="6"/></svg></div>
  <div class="worker" role="img" aria-label="Smiling construction worker holding a yellow hard hat"></div>
  <div class="feature right" style="top:140px"><svg viewBox="0 0 28 28" fill="none" stroke="#f0b417" stroke-width="1.3"><path d="M14 4a7 7 0 0 1 4 13v3h-8v-3a7 7 0 0 1 4-13z"/><line x1="10" y1="24" x2="18" y2="24"/></svg>
    <div><h3>Licensed &amp; Insured</h3><p>Appropriately grow high-quality portals through reliable technology</p></div></div>
  <div class="feature right" style="top:223px"><svg viewBox="0 0 28 28" fill="none" stroke="#f0b417" stroke-width="1.3"><line x1="5" y1="5" x2="23" y2="23"/><line x1="23" y1="5" x2="5" y2="23"/></svg>
    <div><h3>Effective Team Work</h3><p>Appropriately grow high-quality portals through reliable technology</p></div></div>
  <div class="feature right" style="top:308px"><svg viewBox="0 0 28 28" fill="none" stroke="#f0b417" stroke-width="1.3"><circle cx="14" cy="14" r="10"/><path d="M14 8v6l4 3"/></svg>
    <div><h3>24/7 Service</h3><p>Appropriately grow high-quality portals through reliable technology</p></div></div>
</section>

<section class="posts">
  <div class="section-head"><div class="eyebrow">News</div><h2>LATEST POST</h2></div>
  <div class="post-grid">
    <article class="post"><div class="post-img" role="img" aria-label="Power plant chimneys over a field"></div>
      <div class="post-meta"><b>Blog</b> — 08 Jul 2017</div><h3>How to Quickly Add &amp; Edit Beautiful Unstock Images within PageCraft</h3>
      <p>Interactively impact quality catalysts for change without value-added infrastructures. Distinctively reinvent fully tested total linkage vis-a-vis functional solutions.</p></article>
    <article class="post"><div class="post-img" role="img" aria-label="Steel tanks at an industrial facility"></div>
      <div class="post-meta"><b>Blog</b> — 10 Jul 2017</div><h3>How to Quickly Add &amp; Edit Beautiful Unstock Images within PageCraft</h3>
      <p>Interactively impact quality catalysts for change without value-added infrastructures. Distinctively reinvent fully tested total linkage vis-a-vis functional solutions.</p></article>
    <article class="post"><div class="post-img" role="img" aria-label="Old brick factory building"></div>
      <div class="post-meta"><b>Blog</b> — 09 Aug 2017</div><h3>Biomimetics as a tool for the development of new materials</h3>
      <p>Interactively impact quality catalysts for change without value-added infrastructures. Distinctively reinvent fully tested total linkage vis-a-vis functional solutions.</p></article>
  </div>
</section>

<section class="testimonials">
  <div class="section-head"><div class="eyebrow">Feedback</div><h2>TESTIMONIALS</h2></div>
  <div class="quote-grid">
    <div class="quote-card"><div class="quote-badge">“</div>
      <p>Seamlessly simplify scalable processes rather than bleeding-edge information. Objectively disseminate reliable alignments with effective sources. Completely repurpose long-term high-impact action items after real-time users.</p>
      <div class="author"><div class="avatar" role="img" aria-label="Client portrait"></div><div><h4>Dorian Pell</h4><span>CEO, Harbor Works Co.</span></div></div></div>
    <div class="quote-card"><div class="quote-badge">“</div>
      <p>Some days a motivational quote can provide a quick pick-me-up for employees and even management. They can be a breath of fresh air when it comes to a drab afternoon. These are also a great way to jazz up a newsletter or.</p>
      <div class="author"><div class="avatar" role="img" aria-label="Client portrait"></div><div><h4>Nessa Brook</h4><span>CEO, Harbor Works Co.</span></div></div></div>
  </div>
</section>

<section class="partners" aria-label="Partners">
  <div class="partner"></div><div class="partner"></div><div class="partner round"></div><div class="partner round"></div><div class="partner"></div><div class="partner"></div>
</section>

<section class="map">
  <div class="map-area" role="img" aria-label="Street map of the coastal area around the office">
    <svg class="map-pin" viewBox="0 0 16 22"><path d="M8 0a8 8 0 0 1 8 8c0 6-8 14-8 14S0 14 0 8a8 8 0 0 1 8-8z" fill="#e53935"/><circle cx="8" cy="8" r="3" fill="#8b1a1a"/></svg>
  </div>
</section>

<section class="contact">
  <div class="section-head"><div class="eyebrow">Get in touch</div><h2>CONTACT US</h2></div>
  <div class="contact-brand brand"><span class="brand-mark"></span>Marlo Tidy Yard</div>
  <div class="contact-cols">
    <div class="contact-col"><div class="contact-icon"><svg viewBox="0 0 14 14"><path d="M7 1a4 4 0 0 1 4 4c0 3-4 8-4 8S3 8 3 5a4 4 0 0 1 4-4z" fill="#fff"/></svg></div>
      <h3>Visit us at</h3><p>Our showroom is open from 9am to 6pm Monday through Friday</p><p class="value">48 Quarry Lane, Eastfield, North District</p></div>
    <div class="contact-col"><div class="contact-icon"><svg viewBox="0 0 14 14"><path d="M3 1l3 3-2 2c1 2 2 3 4 4l2-2 3 3-2 2C6 13 1 8 1 3z" fill="#fff"/></svg></div>
      <h3>Our phone</h3><p>If you have any questions, just call us and our manager will help you</p><p class="value">(555) 014-2290</p></div>
    <div class="contact-col"><div class="contact-icon"><svg viewBox="0 0 14 14"><rect x="1" y="3" width="12" height="8" fill="#fff"/><path d="M1 3l6 5 6-5" fill="none" stroke="#f0b417"/></svg></div>
      <h3>Our contact email</h3><p>Tell us the reason for your query and we will get you an answer</p><p class="value">hello@marlotidyyard.test</p></div>
  </div>
</section>

<footer class="site-footer">
  <span class="social-dot"></span><span class="social-dot"></span><span class="social-dot"></span><span class="social-dot"></span><span class="social-dot"></span>
</footer>

</div>
</body>
</html>
```